Visitenkarte/Briefpapier für Coaching
Vielen Dank für die hervorragende Umsetzung meines Briefings und die super schnelle Bearbeitung meiner Kommentare. Das Ergebnis ist super! Gern empfehle ich Sie weiter.
Zielgruppe
Die Visitenkarte/Briefpapier soll sowohl Unternehmen als auch Privatpersonen aller Altersklassen ansprechen. Coaching hilft blockierende Verhaltensweisen zu überwinden, Ziele zu erreichen und alternative Wege im Handeln aufzuzeigen. Als Methode wird u.a. das flutstern-coaching eingesetzt (siehe www.flutstern.com). Anwendungsbeispiele sind: Flugangst, Prüfungsangst, Zahnbehandlungsangst, Beseitigung von Leistungs- und Kreativitätsblockaden, Burn-Out-Prophylaxe, Wettkampfvorbereitung, Teamcoaching usw.
Aufgabenstellung
Die Visitenkarte/Briefpapier soll Vertrauen, Zuverlässigkeit sowie die Merkmale des Coachings vermitteln. Mein Logo finden Sie als Datei angehängt. Dies sollte auf Seite 1 zu finden sein.
Ebenso meine Kontaktdaten:
Web: www.pfadlicht-coaching.de. Für Tel. Mobil, E-Mail und Internet hätte ich gern Symbole.
Auf Seite 2 der Visitenkarte möchte ich gern den Spruch: Wollen Sie Ihren Weg mit (hier flutstern-Logo aus Datei-Anhang einfügen, bitte Styleguide beachten)-Coaching finden?
Bei der Farbgestaltung der Visitenkarte/Briefpapier sollten sich die Farben aus dem Pfadlicht-Logo wiederfinden. Es darf auch gern ein farbiger Hintergrund sein.

```html
<!DOCTYPE html>
<html lang="de">
<head>
<meta charset="utf-8">
<title>Pfadlicht Coaching – Visitenkarte</title>
<link rel="stylesheet" href="https://fonts.googleapis.com/css2?family=Alegreya+Sans:wght@400;700&display=swap">
<style>
  :root {
    --card-white: #ffffff;
    --brand-green: #7aa322;
    --brand-blue: #1f5d86;
    --bar-grey: #4a4a4c;
    --text-light: #ffffff;
  }
  * { margin: 0; padding: 0; box-sizing: border-box; }
  html, body {
    width: 1200px;
    height: 778px;
    overflow: hidden;
    background: var(--card-white);
  }
  .business-card {
    position: relative;
    width: 1200px;
    height: 778px;
    background: var(--card-white);
    font-family: "Alegreya Sans", sans-serif;
    overflow: hidden;
  }
  .wave-background {
    position: absolute;
    inset: 0;
    width: 1200px;
    height: 778px;
  }
  .brand-mark-dot {
    position: absolute;
    left: 57px;
    top: 60px;
    width: 158px;
    height: 158px;
    border-radius: 50%;
    background: var(--brand-green);
  }
  .brand-divider {
    position: absolute;
    left: 245px;
    top: 62px;
    width: 2px;
    height: 168px;
    background: #8a8a8a;
  }
  .brand-name {
    position: absolute;
    left: 280px;
    top: 62px;
    font-size: 104px;
    font-weight: 700;
    line-height: 1;
    color: var(--brand-blue);
    letter-spacing: 1px;
  }
  .contact-list {
    position: absolute;
    right: 72px;
    top: 436px;
    list-style: none;
    text-align: right;
    color: var(--text-light);
    font-size: 34px;
    line-height: 45px;
    letter-spacing: 0.3px;
  }
  .address-bar {
    position: absolute;
    left: 71px;
    top: 658px;
    width: 1057px;
    height: 69px;
    background: var(--bar-grey);
    color: var(--text-light);
    display: flex;
    align-items: center;
    padding-left: 36px;
    font-size: 34px;
    white-space: nowrap;
  }
  .address-bar .holder-name { font-weight: 700; }
  .address-bar .separator {
    display: inline-block;
    width: 5px;
    height: 22px;
    background: #1e1e1e;
    margin: 0 22px;
  }
</style>
</head>
<body>
<main class="business-card">
  <svg class="wave-background" viewBox="0 0 1200 778" aria-hidden="true">
    <path d="M0 421 C160 428 340 458 446 528 C610 372 860 250 1200 234"
          fill="none" stroke="var(--brand-green)" stroke-width="5"/>
    <path d="M0 436 C160 443 340 472 446 543 C610 387 860 264 1200 248 L1200 778 L0 778 Z"
          fill="var(--brand-green)"/>
  </svg>

  <div class="brand-mark-dot"></div>
  <div class="brand-divider"></div>
  <div class="brand-name">Pfadlicht</div>

  <ul class="contact-list">
    <li>Telefon: 0461 / 5 47 80</li>
    <li>Mobil: 0170 / 412 75 03</li>
    <li>E-Mail: info@pfadlicht-coaching.de</li>
    <li>Web: www.pfadlicht-coaching.de</li>
  </ul>

  <div class="address-bar">
    <span class="holder-name">Lena Harmsen</span>
    <span class="separator"></span>
    <span>Möwenstieg 14</span>
    <span class="separator"></span>
    <span>D-24937 Flensburg</span>
  </div>
</main>
</body>
</html>
```